Business Card design for amazing new Dental Office

Please read this brief closely!

Our client is a modern new dental office/
They love their new logo.
Now it's time to create a business card for them.

It should be a two sided card:
Side one should have the logo and name and maybe a color background or design.
Side two should have all the contact information which is here:

Marcus Holloway, D.D.S
General and Cosmetic Dentistry
4187 W. Pinecrest Avenue
Ventura, CA 93011
(805) 912-4386
drmarcus@bluefernsmiles-example.com
www.bluefernsmiles-example.com

Feel free to arrange that info as you like and to style both sides of the card according to your creativity. This is a chance for you to show your design skills!

Client is open to font choices and is looking for a style that is amazing and premium. Colors can be selected from the logo, or any variation of those.

You will not win this contest with a less than beautiful card design so please feel free to make multiple submissions.

Logo files attached and please message me with any questions.
Thanks!

Target Market(s)

Families and Professionals seeking dental services

Industry/Entity Type

Dental

Contact Information for Business Card

Logo, style, contact info as per the brief

Font styles to use
Sans Serif

Requirements
Must have
• Client's logo and contact details as per brief
Nice to have
• Unique style reflecting high end dental clinic near the beach
Should not have
• Must not look like a template

```html
<!DOCTYPE html>
<html lang="en">
<head>
<meta charset="utf-8">
<title>Blue Fern Smiles – Business Card</title>
<link href="https://fonts.googleapis.com/css2?family=Jost:wght@300;400;600&display=swap" rel="stylesheet">
<style>
  :root {
    --backdrop: #e4e4df;
    --cream: #f3e6b6;
    --gold: #dcc068;
    --olive-gold: #cfc57c;
    --sage: #a9ccaa;
    --teal: #72bcb3;
    --sky: #d0ecf8;
    --glow: #ffffff;
    --mark-teal: #6cc2c4;
    --mark-gold: #d3c25a;
    --name-grey: #adadad;
    --ink: #111111;
    --paper: #ffffff;
  }
  * { margin: 0; padding: 0; box-sizing: border-box; }
  html, body { width: 1200px; height: 1200px; overflow: hidden; }
  body {
    background: var(--backdrop);
    font-family: "Jost", sans-serif;
    position: relative;
  }
  .card {
    position: absolute;
    left: 194px;
    width: 812px;
    height: 464px;
    border-radius: 48px;
    overflow: hidden;
  }
  .card-gradient {
    background:
      linear-gradient(135deg, var(--cream) 0%, rgba(243,230,182,0) 45%),
      linear-gradient(45deg, var(--sky) 0%, rgba(208,236,248,0) 45%),
      linear-gradient(315deg, var(--teal) 0%, rgba(114,188,179,0) 50%),
      linear-gradient(225deg, var(--olive-gold) 0%, rgba(207,197,124,0) 50%),
      linear-gradient(180deg, var(--gold) 0%, var(--sage) 100%);
  }
  .card-front { top: 87px; }
  .front-glow {
    position: absolute;
    inset: 0;
    background: radial-gradient(circle at 50% 48%, var(--glow) 0%, rgba(255,255,255,0.85) 18%, rgba(255,255,255,0) 52%);
  }
  .front-brand {
    position: absolute;
    left: 0; right: 0;
    top: 135px;
    text-align: center;
    color: var(--name-grey);
    font-weight: 300;
  }
  .brand-dot {
    display: block;
    width: 72px; height: 72px;
    border-radius: 50%;
    background: var(--mark-teal);
    margin: 0 auto 42px;
  }
  .brand-name {
    display: block;
    font-size: 46px;
    letter-spacing: 6px;
    line-height: 1;
  }
  .brand-sub {
    display: block;
    font-size: 24px;
    letter-spacing: 26px;
    margin-top: 14px;
    padding-left: 26px;
  }
  .card-back { top: 635px; }
  .contact-panel {
    position: absolute;
    left: 213px;
    width: 385px;
    top: 0; bottom: 0;
    background: var(--paper);
    text-align: center;
    color: var(--ink);
  }
  .panel-dot {
    display: block;
    width: 68px; height: 68px;
    border-radius: 50%;
    background: var(--mark-gold);
    margin: 40px auto 0;
  }
  .doctor-name {
    font-size: 25px;
    font-weight: 600;
    margin-top: 60px;
    line-height: 1.2;
  }
  .specialty { font-size: 20px; line-height: 1.3; margin-top: 2px; }
  .address { font-size: 20px; line-height: 29px; margin-top: 26px; }
  .email { font-size: 17px; margin-top: 30px; line-height: 1.3; }
  .website { font-size: 17px; font-weight: 600; letter-spacing: 0.5px; line-height: 1.5; }
</style>
</head>
<body>
  <section class="card card-front card-gradient">
    <div class="front-glow"></div>
    <div class="front-brand">
      <span class="brand-dot"></span>
      <span class="brand-name">BLUE FERN</span>
      <span class="brand-sub">SMILES</span>
    </div>
  </section>

  <section class="card card-back card-gradient">
    <div class="contact-panel">
      <span class="panel-dot"></span>
      <p class="doctor-name">Marcus Holloway, D.D.S</p>
      <p class="specialty">General and Cosmetic Dentistry</p>
      <p class="address">4187 W. Pinecrest Avenue<br>Ventura, CA 93011<br>(805) 912-4386</p>
      <p class="email">drmarcus@bluefernsmiles-example.com</p>
      <p class="website">www.bluefernsmiles-example.com</p>
    </div>
  </section>
</body>
</html>
```